Brindle Logistics Business Card Design

We are a trucking and warehousing company. We run freight in the US manly from the Pacific NW to TX and back up the the PNW. We also do warehousing where we store, move, and distribute freight. Looking for a clean and modern design of business card. We would like to look rich and elegant. Attached is our logo.

Industry/Entity Type

Trucking Company

Contact Information for Business Card

Looking for a clean and modern design of business card. We would like to look rich and elegant.

Font styles to use
Sans Serif

Colors

Designer to choose colors to be used in the design.

Requirements
Must have
• logo but it should not dominate the card
Should not have
• logo should not dominate the card

```html
<!DOCTYPE html>
<html lang="en">
<head>
<meta charset="utf-8">
<title>Brindle Logistics Business Card</title>
<link href="https://fonts.googleapis.com/css2?family=Roboto:wght@400;500&display=swap" rel="stylesheet">
<style>
  :root {
    --page: #ffffff;
    --black: #000000;
    --card: #1b1b1b;
    --card-dark: #141414;
    --orange: #f7941d;
    --blue: #0b6fc2;
    --white: #ffffff;
  }
  * { margin: 0; padding: 0; box-sizing: border-box; }
  html, body { width: 911px; height: 1200px; overflow: hidden; background: var(--page); }
  body { position: relative; font-family: "Roboto", Arial, sans-serif; }

  .card { position: absolute; left: 0; width: 911px; height: 549px; background: var(--card); overflow: hidden; }
  .card--front { top: 35px; }
  .card--back { top: 617px; }

  .band-edge { position: absolute; background: var(--black); }
  .card--front .band-edge--top { left: 0; top: 0; width: 100%; height: 30px; }
  .card--front .band-edge--bottom { left: 0; bottom: 0; width: 100%; height: 31px; }
  .card--back .band-edge--left { left: 0; top: 0; width: 29px; height: 100%; }
  .card--back .band-edge--right { right: 0; top: 0; width: 27px; height: 100%; }

  .center-band { position: absolute; left: 0; width: 100%;
    background: linear-gradient(180deg, var(--card-dark) 0%, var(--card) 12%, var(--card) 88%, var(--card-dark) 100%);
    box-shadow: 0 -4px 8px rgba(0,0,0,.6), 0 4px 8px rgba(0,0,0,.6); }
  .card--front .center-band { top: 140px; height: 271px; }
  .card--back .center-band { top: 139px; height: 269px; }

  .decor { position: absolute; left: 0; top: 0; width: 100%; height: 100%; }

  .name-plate { position: absolute; left: 0; top: 225px; width: 372px; height: 95px; background: var(--black);
    display: flex; align-items: center; padding-left: 34px; }
  .name-plate__text { color: var(--orange); font-size: 37px; font-weight: 400; white-space: nowrap; letter-spacing: -0.2px; }

  .contact-list { position: absolute; left: 533px; top: 159px; list-style: none; }
  .contact-item { display: flex; align-items: center; height: 39px; margin-bottom: 24px; }
  .contact-item__icon { width: 39px; height: 39px; flex: none; }
  .contact-item__text { margin-left: 15px; color: var(--white); font-size: 23px; }

  .brand-mark { position: absolute; left: 0; top: 247px; width: 100%; display: flex; justify-content: center; align-items: center; gap: 14px; }
  .brand-mark__dot { width: 34px; height: 34px; border-radius: 50%; background: var(--blue); }
  .brand-mark__name { color: var(--white); font-size: 38px; font-weight: 500; white-space: nowrap; }
</style>
</head>
<body>

<section class="card card--front" aria-label="Card front">
  <div class="band-edge band-edge--top"></div>
  <div class="center-band"></div>
  <svg class="decor" viewBox="0 0 911 549" aria-hidden="true">
    <path d="M60 140 L870 40" stroke="#0a0a0a" stroke-width="4" fill="none"/>
    <path d="M60 510 L870 411" stroke="#0a0a0a" stroke-width="4" fill="none"/>
    <path d="M447 150 L405 276 L447 400" stroke="#0a0a0a" stroke-width="5" fill="none"/>
  </svg>
  <div class="band-edge band-edge--bottom"></div>

  <div class="name-plate"><span class="name-plate__text">Brindle Logistics, LLC</span></div>

  <ul class="contact-list">
    <li class="contact-item">
      <svg class="contact-item__icon" viewBox="0 0 40 40" aria-hidden="true">
        <circle cx="20" cy="20" r="20" fill="var(--blue)"/>
        <path d="M14 11 l4 0 l2 6 l-3 2 q2 5 6 7 l2-3 l6 2 l0 4 q-1 2-3 2 q-10-1-15-12 q-1-6 1-8z" fill="#0a0a0a"/>
      </svg>
      <span class="contact-item__text">Phone number</span>
    </li>
    <li class="contact-item">
      <svg class="contact-item__icon" viewBox="0 0 40 40" aria-hidden="true">
        <circle cx="20" cy="20" r="20" fill="var(--blue)"/>
        <circle cx="20" cy="20" r="10" fill="none" stroke="#0a0a0a" stroke-width="2.2"/>
        <path d="M10 20 h20 M20 10 q-6 10 0 20 M20 10 q6 10 0 20" fill="none" stroke="#0a0a0a" stroke-width="1.8"/>
      </svg>
      <span class="contact-item__text">www.website.com</span>
    </li>
    <li class="contact-item">
      <svg class="contact-item__icon" viewBox="0 0 40 40" aria-hidden="true">
        <circle cx="20" cy="20" r="20" fill="var(--blue)"/>
        <rect x="10" y="13" width="20" height="14" fill="#0a0a0a"/>
        <path d="M10 13 L20 21 L30 13 M10 27 L17 19 M30 27 L23 19" stroke="var(--blue)" stroke-width="1.6" fill="none"/>
      </svg>
      <span class="contact-item__text">contact@email.com</span>
    </li>
    <li class="contact-item">
      <svg class="contact-item__icon" viewBox="0 0 40 40" aria-hidden="true">
        <circle cx="20" cy="20" r="20" fill="var(--blue)"/>
        <path d="M20 32 C14 24 12 21 12 17 a8 8 0 0 1 16 0 c0 4-2 7-8 15z" fill="#0a0a0a"/>
        <circle cx="20" cy="17" r="3" fill="var(--blue)"/>
      </svg>
      <span class="contact-item__text">Adress</span>
    </li>
  </ul>
</section>

<section class="card card--back" aria-label="Card back">
  <div class="center-band"></div>
  <svg class="decor" viewBox="0 0 911 549" aria-hidden="true">
    <path d="M80 140 L880 37" stroke="#0a0a0a" stroke-width="4" fill="none"/>
    <path d="M40 510 L880 408" stroke="#0a0a0a" stroke-width="4" fill="none"/>
    <path d="M290 150 L240 274 L290 400 L625 400 L675 274 L625 150" stroke="#0a0a0a" stroke-width="5" fill="none"/>
  </svg>
  <div class="band-edge band-edge--left"></div>
  <div class="band-edge band-edge--right"></div>

  <div class="brand-mark">
    <span class="brand-mark__dot"></span>
    <span class="brand-mark__name">Brindle Logistics</span>
  </div>
</section>

</body>
</html>
```